Business Card Design Project - KLB

I am looking for a more sophisticated card design for my company,
"The Kestrel Bureau"

We are a consultancy focused on strategy and change in Associations and professional organisations.

I am a lawyer and psychologist with a PhD and so am looking for something that communicates seriousness and credibility but also quirky creative solutions for strategic problems, which is my field of speciality.

I am looking for something that is quietly spoken, rather than loud colours ('credible' and 'creative' are the two adjectives that I think of as competing here).

I particularly like an embossed card style - heavy white card with plain white or white and black or white and grey text.

The key logo image for the company is a question mark and I am open to suggestions and ideas on design.

I have attached a file that includes a couple of styles that have caught my eye and my thoughts on them. Hopefully they communicate what I'm looking for.
Updates

Thank you for all the great suggestions and designs.

I really appreciated the effort and creative energy you put into your designs. I have now closed the project after selecting a design and advising the successful designer of the card that I am happy with.

Regards

Target Market(s)

Organisations (CEO's and Boards), Governments, Legal professionals, Membership Associations and aspiring professionals.

Industry/Entity Type

Lawyer

Requirements
Must have
• The key logo element is a question mark (?) and this needs to be incorporated.

Embossed style - cut outs or other design ideas interest me too.

The attached file has a number of sample ideas and comments on each one that I like.
Should not have
• I like crisp, modern fonts (Myriads etc...) and do not like embellished fonts or Times etc...

```html
<!DOCTYPE html>
<html lang="en">
<head>
<meta charset="utf-8">
<title>The Kestrel Bureau – Business Card</title>
<link rel="stylesheet" href="https://fonts.googleapis.com/css2?family=Arimo:wght@400;700&display=swap">
<style>
  :root {
    --backdrop: #2a2421;
    --card: #f4f4f2;
    --card-edge: #e2e2df;
    --mark-grey: #c9c9c7;
    --brand-grey: #8c8c8a;
    --name-grey: #6f6f6d;
    --detail-grey: #7d7d7b;
    --accent-red: #cf1f1d;
  }
  * { box-sizing: border-box; margin: 0; padding: 0; }
  html, body {
    width: 957px;
    height: 1200px;
    overflow: hidden;
    background: var(--backdrop);
    font-family: "Arimo", Arial, sans-serif;
  }
  .canvas {
    position: relative;
    width: 957px;
    height: 1200px;
  }
  .card {
    position: absolute;
    left: 68px;
    width: 820px;
    height: 455px;
    background: linear-gradient(160deg, #fbfbfa 0%, var(--card) 55%, var(--card-edge) 100%);
    border-radius: 72px 6px 6px 6px;
    box-shadow: 0 18px 40px rgba(0, 0, 0, 0.55);
  }
  .card--accent-bar { top: 96px; }
  .card--accent-dot { top: 648px; }

  .brand {
    position: absolute;
    left: 48px;
    top: 48px;
    display: flex;
    align-items: center;
    gap: 22px;
  }
  .brand__square {
    width: 150px;
    height: 150px;
    background: var(--mark-grey);
    border-radius: 4px;
  }
  .brand__name {
    font-size: 40px;
    font-weight: 700;
    color: var(--brand-grey);
    letter-spacing: 1px;
  }

  .contact {
    position: absolute;
    right: 70px;
    top: 262px;
    width: 420px;
    color: var(--detail-grey);
  }
  .contact__name {
    font-size: 28px;
    font-weight: 700;
    color: var(--name-grey);
    letter-spacing: 4px;
    margin-bottom: 10px;
  }
  .contact__phones {
    display: flex;
    justify-content: space-between;
    align-items: center;
    font-size: 11px;
    letter-spacing: 1.5px;
    margin-bottom: 14px;
  }
  .contact__address {
    font-size: 11px;
    letter-spacing: 1.5px;
    margin-bottom: 16px;
  }
  .contact__email {
    font-size: 11px;
    letter-spacing: 1.5px;
    text-align: right;
  }
  .accent-bar {
    position: absolute;
    right: -22px;
    top: 4px;
    width: 4px;
    height: 78px;
    background: var(--accent-red);
    border-radius: 2px;
  }
  .accent-dot {
    width: 8px;
    height: 8px;
    border-radius: 50%;
    background: var(--accent-red);
  }
</style>
</head>
<body>
<main class="canvas">

  <section class="card card--accent-bar">
    <div class="brand">
      <div class="brand__square"></div>
      <div class="brand__name">The Kestrel Bureau</div>
    </div>
    <div class="contact">
      <span class="accent-bar"></span>
      <p class="contact__name">Dr. Mara Ellison</p>
      <p class="contact__phones"><span>M::: +61400 123 456</span><span>P::: +612 9000 4417</span></p>
      <p class="contact__address">P.O. Box 4410, Harlow Vale, Sydney, Australia</p>
      <p class="contact__email">mara@kestrelbureau.com.au</p>
    </div>
  </section>

  <section class="card card--accent-dot">
    <div class="brand">
      <div class="brand__square"></div>
      <div class="brand__name">The Kestrel Bureau</div>
    </div>
    <div class="contact">
      <p class="contact__name">Dr. Mara Ellison</p>
      <p class="contact__phones"><span>M::: +61400 123 456</span><span class="accent-dot"></span><span>P::: +612 9000 4417</span></p>
      <p class="contact__address">P.O. Box 4410, Harlow Vale, Sydney, Australia</p>
      <p class="contact__email">mara@kestrelbureau.com.au</p>
    </div>
  </section>

</main>
</body>
</html>
```